Camp Brookhaven 2018

We need a postcard design to advertise our summer programs. We are a Christian camp with day camp and overnight camps.

Target Market(s)

parents of elementary age kids

Industry/Entity Type

Christian

Colors
ec1f27
f37122
faa54b
fbee3d
f78f20
f04a50
fbed22
fbee3e

Requirements
Must have
• Day Camp 2018 "Shine Bright Daily"
• June 25 - August 24
• $135 per week
• Mon-Fri 8 am to 4 pm. Open to all kids entering grades 1 to 8. Day camp is chock full of activities like swimming, rock wall, archery, sports, crafts, air rifles and much more! Daily lunch and snack included. Before and after-care available at an extra rate.
• Register and pay in full by April 1st, save $270!
• Overnight Camp 2018
• July 15 - 21 & July 22 - 28
• $330 per week
• Open to all kids ages 8 to 14. Spend the week making new friends, sleeping in cabins, climbing the rock wall and swimming at the beach! Our guest speakers will lead twice daily chapel sessions that will challenge campers to grow in their faith.
• 41 Maple Crest Rd. Millbrook, VT 03917
• 603-418-2956
• www.brookhavencamp.org
Nice to have
• bright and colorful

```html
<!DOCTYPE html>
<html lang="en">
<head>
<meta charset="utf-8">
<title>Camp Brookhaven 2018 Postcards</title>
<link rel="stylesheet" href="https://fonts.googleapis.com/css2?family=Alfa+Slab+One&family=Ultra&family=Rubik:wght@700;900&family=Patrick+Hand&display=swap">
<style>
  :root{
    --red:#ec1f27;
    --orange:#f37122;
    --orange-soft:#faa54b;
    --orange-mid:#f78f20;
    --yellow:#fbee3d;
    --coral:#f04a50;
    --ink:#111111;
    --paper:#ffffff;
    --backdrop:#efe7da;
  }
  html,body{margin:0;padding:0;width:1200px;height:1200px;overflow:hidden;background:var(--backdrop);}
  .postcard{position:absolute;width:806px;height:537px;background:var(--paper);box-shadow:0 6px 18px rgba(0,0,0,.25);overflow:hidden;}
  .postcard--day{left:62px;top:50px;}
  .postcard--overnight{left:330px;top:606px;}
  .postcard svg{position:absolute;left:0;top:0;width:806px;height:537px;}
  .display{font-family:"Ultra","Alfa Slab One",Rockwell,serif;font-weight:400;}
  .heavy{font-family:"Rubik",sans-serif;font-weight:900;}
  .bold{font-family:"Rubik",sans-serif;font-weight:700;}
  .hand{font-family:"Patrick Hand",cursive;}
  .copy{position:absolute;font-family:"Patrick Hand",cursive;text-transform:uppercase;margin:0;}
  .copy--day{left:391px;top:346px;width:174px;font-size:12.5px;line-height:11.2px;letter-spacing:.6px;color:var(--ink);text-align:justify;}
  .copy--overnight{left:12px;top:20px;width:374px;font-size:15px;line-height:14px;letter-spacing:.5px;color:var(--paper);text-align:justify;}
  .brand{font-family:"Rubik",sans-serif;font-weight:700;fill:var(--orange);}
</style>
</head>
<body>

<section class="postcard postcard--day" aria-label="Day camp postcard">
  <svg viewBox="0 0 806 537" xmlns="http://www.w3.org/2000/svg">
    <defs>
      <radialGradient id="halftoneDay" cx="40%" cy="45%" r="70%">
        <stop offset="0" stop-color="#faa54b"/>
        <stop offset="1" stop-color="#f37122"/>
      </radialGradient>
      <path id="cloud" d="M60,230 a50,50 0 0 1 -20,-90 a60,60 0 0 1 60,-90 a70,70 0 0 1 110,-20 a70,70 0 0 1 100,30 a60,60 0 0 1 40,90 a50,50 0 0 1 -40,90 a60,60 0 0 1 -100,30 a70,70 0 0 1 -110,-10 a50,50 0 0 1 -40,-30 z"/>
      <polygon id="burst" points="-75,0 -50,-12 -62,-30 -30,-22 -25,-45 0,-25 15,-48 25,-22 55,-38 48,-12 78,-8 52,6 70,28 35,18 25,42 5,20 -15,45 -22,18 -55,32 -45,8"/>
    </defs>
    <g class="panel-strips" stroke="var(--ink)" stroke-width="2">
      <polygon points="0,0 320,0 316,16 0,16" fill="var(--orange-soft)"/>
      <polygon points="334,0 572,0 568,16 330,16" fill="var(--yellow)"/>
      <polygon points="586,0 806,0 806,16 582,16" fill="var(--orange-mid)"/>
      <polygon points="0,516 364,514 366,537 0,537" fill="var(--red)"/>
      <polygon points="380,516 684,514 684,537 380,537" fill="var(--yellow)"/>
      <polygon points="698,516 806,514 806,537 698,537" fill="var(--coral)"/>
    </g>
    <polygon class="panel-main" points="0,26 556,26 548,284 0,284" fill="url(#halftoneDay)" stroke="var(--ink)" stroke-width="2"/>
    <polygon class="photo" role="img" aria-label="Photo of three smiling campers in swimsuits and goggles" points="564,24 806,24 806,284 556,288" fill="#8fae6a" stroke="var(--ink)" stroke-width="2"/>
    <polygon class="photo" role="img" aria-label="Photo of two girls smiling in the lake" points="0,296 364,292 368,506 0,508" fill="#7f9a88" stroke="var(--ink)" stroke-width="2"/>
    <polygon class="panel-info" points="380,294 806,294 806,504 386,504" fill="var(--orange-mid)" stroke="var(--ink)" stroke-width="2"/>
    <path class="panel-brand" d="M806,298 L646,298 Q596,398 646,496 L806,496 Z" fill="var(--ink)"/>
    <g class="speed-lines" fill="var(--ink)">
      <polygon points="110,40 128,78 120,80"/><polygon points="132,34 144,74 136,75"/>
      <polygon points="486,104 530,96 530,102"/><polygon points="480,120 540,116 540,122"/>
      <polygon points="10,300 70,248 74,254"/><polygon points="30,320 80,268 84,274"/>
      <polygon points="574,404 592,344 597,346"/><polygon points="588,420 604,356 609,358"/>
    </g>
    <g class="title-cloud" transform="translate(8,-14) scale(1.3,1.16) rotate(-4 200 150)">
      <use href="#cloud" fill="var(--ink)" transform="translate(-6,6)"/>
      <use href="#cloud" fill="var(--paper)" stroke="var(--ink)" stroke-width="4"/>
    </g>
    <g class="title" transform="rotate(-8 260 170)" fill="var(--ink)" text-anchor="middle">
      <text class="display" x="262" y="152" font-size="58">SHINE</text>
      <text class="display" x="262" y="192" font-size="28">BRIGHT DAILY</text>
      <text class="display" x="300" y="218" font-size="14">DAY CAMP 2018</text>
    </g>
    <g class="date-bubble">
      <polygon points="630,76 660,76 676,108" fill="var(--paper)" stroke="var(--ink)" stroke-width="3"/>
      <ellipse cx="612" cy="48" rx="66" ry="38" fill="var(--paper)" stroke="var(--ink)" stroke-width="3"/>
      <text class="bold" x="612" y="38" font-size="10" text-anchor="middle">JUNE 25,2018</text>
      <text class="bold" x="612" y="51" font-size="10" text-anchor="middle">TO</text>
      <text class="bold" x="612" y="64" font-size="10" text-anchor="middle">AUGUST 24,2018</text>
    </g>
    <g class="price-burst" transform="translate(560,270) rotate(-15) scale(1.15,0.95)">
      <use href="#burst" fill="var(--paper)" stroke="var(--ink)" stroke-width="2.5"/>
    </g>
    <text class="bold" x="560" y="276" font-size="15" text-anchor="middle" transform="rotate(-17 560 272)">$135 PER WEEK</text>
    <g class="register-bar">
      <polygon points="24,470 340,466 336,492 20,496" fill="var(--paper)" stroke="var(--ink)" stroke-width="3"/>
      <text class="bold" x="180" y="485" font-size="11" text-anchor="middle" fill="var(--ink)">REGISTER AND PAY IN FULL BY APRIL 1ST, SAVE $270!</text>
    </g>
    <g class="brand-mark">
      <circle cx="654" cy="398" r="8" fill="var(--red)"/>
      <text class="brand" x="668" y="392" font-size="21">Camp</text>
      <text class="brand" x="668" y="416" font-size="21">Brookhaven</text>
    </g>
  </svg>
  <p class="copy copy--day">Mon-Fri 8 am to 4 pm. Open to all kids entering grades 1 to 8. Day camp is chock full of activities like swimming, rock wall, archery, sports, crafts, air rifles and much more! Daily lunch and snack included. Before and after-care available at an extra rate.</p>
</section>

<section class="postcard postcard--overnight" aria-label="Overnight camp postcard">
  <svg viewBox="0 0 806 537" xmlns="http://www.w3.org/2000/svg">
    <defs>
      <radialGradient id="halftoneNight" cx="45%" cy="50%" r="70%">
        <stop offset="0" stop-color="#faa54b"/>
        <stop offset="1" stop-color="#f37122"/>
      </radialGradient>
      <path id="cloudB" d="M60,230 a50,50 0 0 1 -20,-90 a60,60 0 0 1 60,-90 a70,70 0 0 1 110,-20 a70,70 0 0 1 100,30 a60,60 0 0 1 40,90 a50,50 0 0 1 -40,90 a60,60 0 0 1 -100,30 a70,70 0 0 1 -110,-10 a50,50 0 0 1 -40,-30 z"/>
      <polygon id="burstB" points="-75,0 -50,-12 -62,-30 -30,-22 -25,-45 0,-25 15,-48 25,-22 55,-38 48,-12 78,-8 52,6 70,28 35,18 25,42 5,20 -15,45 -22,18 -55,32 -45,8"/>
    </defs>
    <polygon class="panel-red" points="0,0 400,0 394,152 0,152" fill="var(--red)" stroke="var(--ink)" stroke-width="2"/>
    <polygon class="panel-accent" points="414,0 512,0 506,150 408,152" fill="var(--orange-soft)" stroke="var(--ink)" stroke-width="2"/>
    <polygon class="photo" role="img" aria-label="Photo of three smiling girls at camp" points="520,0 806,0 806,172 514,166" fill="#9fa8a0" stroke="var(--ink)" stroke-width="2"/>
    <polygon class="panel-main" points="0,160 356,162 366,346 0,352" fill="url(#halftoneNight)" stroke="var(--ink)" stroke-width="2"/>
    <polygon class="panel-yellow" points="338,168 806,182 806,314 374,326" fill="var(--yellow)" stroke="var(--ink)" stroke-width="2"/>
    <polygon class="photo" role="img" aria-label="Photo of a laughing girl riding a green tube down a water slide" points="0,360 244,352 236,537 0,537" fill="#7fae5e" stroke="var(--ink)" stroke-width="2"/>
    <polygon class="panel-info" points="256,338 806,326 806,537 250,537" fill="var(--orange-mid)" stroke="var(--ink)" stroke-width="2"/>
    <path class="panel-brand" d="M806,324 L590,326 Q520,430 570,537 L806,537 Z" fill="var(--ink)"/>
    <g class="speed-lines" fill="var(--ink)">
      <polygon points="60,118 86,160 80,162"/><polygon points="80,112 100,156 94,158"/>
      <polygon points="222,104 218,158 224,158"/><polygon points="240,110 232,160 238,161"/>
      <polygon points="320,196 362,170 364,176"/><polygon points="326,212 372,190 374,196"/>
      <polygon points="0,292 46,270 48,276"/>
      <polygon points="272,372 262,404 268,406"/><polygon points="286,372 272,404 278,406"/>
    </g>
    <g class="price-burst" transform="translate(440,100) rotate(-15) scale(1.2,0.95)">
      <use href="#burstB" fill="var(--paper)" stroke="var(--ink)" stroke-width="2.5"/>
    </g>
    <text class="bold" x="440" y="106" font-size="14" text-anchor="middle" transform="rotate(-17 440 102)">$330 PER WEEK</text>
    <g class="title-cloud" transform="translate(-8,120) scale(0.96,0.88) rotate(-4 200 150)">
      <use href="#cloudB" fill="var(--ink)" transform="translate(-6,6)"/>
      <use href="#cloudB" fill="var(--paper)" stroke="var(--ink)" stroke-width="4"/>
    </g>
    <g class="title" transform="rotate(-8 180 260)" fill="var(--ink)" text-anchor="middle">
      <text class="display" x="180" y="256" font-size="42">SHINE</text>
      <text class="display" x="182" y="284" font-size="20">BRIGHT DAILY</text>
      <text class="display" x="210" y="303" font-size="9.5">OVERNIGHT CAMP 2018</text>
    </g>
    <text class="display" x="596" y="234" font-size="40" text-anchor="middle" fill="var(--ink)">OVERNIGHT</text>
    <text class="heavy" x="596" y="274" font-size="32" text-anchor="middle" fill="var(--red)">CAMP 2018</text>
    <text class="heavy" x="284" y="406" font-size="16" fill="var(--ink)">JULY 15 – 21 &amp; JULY 22 – 28</text>
    <text class="hand" x="394" y="446" font-size="17" text-anchor="middle" fill="var(--ink)">41 MAPLE CREST RD.</text>
    <text class="hand" x="394" y="466" font-size="17" text-anchor="middle" fill="var(--ink)">MILLBROOK, VT 03917</text>
    <text class="hand" x="276" y="499" font-size="15" fill="var(--ink)">603-418-2956</text>
    <text class="hand" x="392" y="499" font-size="15" fill="var(--ink)">www.brookhavencamp.org</text>
    <g class="brand-mark">
      <circle cx="590" cy="432" r="10" fill="var(--red)"/>
      <text class="brand" x="606" y="424" font-size="27">Camp</text>
      <text class="brand" x="606" y="454" font-size="27">Brookhaven</text>
    </g>
  </svg>
  <p class="copy copy--overnight">Open to all kids ages 8 to 14. Spend the week making new friends, sleeping in cabins, climbing the rock wall and swimming at the beach! Our guest speakers will lead twice daily chapel sessions that will challenge campers to grow in their faith.</p>
</section>

</body>
</html>
```